TIDAL VERGE needs bisness cards pronto

Bisness name is "TIDAL VERGE" new bisness the bisness includes lawn mowing, garden matanace, and any jobs around the house.
I need a card that is colorful and vibrant and the bisness of lawn mowing maybe with some nature with it. It also needs my contact details"Darren Quellby mobile 0413562049 call for free quote and email norma.vance@fernmail.com.au and a catchy tag line

Industry/Entity Type

House

Requirements
Must have
• Bisness name "TIDAL VERGE"
Contact details "0413562049"
Email norma.vance@fernmail.com.au
Call for free quote

```html
<!DOCTYPE html>
<html lang="en">
<head>
<meta charset="utf-8">
<title>Tidal Verge – Business Card Concepts</title>
<link rel="stylesheet" href="https://fonts.googleapis.com/css2?family=Archivo+Black&family=Michroma&family=PT+Sans:ital,wght@0,700;1,700&family=Cinzel:wght@600&display=swap">
<style>
  :root {
    --board-light: #ece0cd;
    --board-warm: #f0cc9c;
    --brand-yellow: #ffe600;
    --brand-green: #1f5a14;
    --contact-yellow: #fff200;
    --label-orange: #e07a2c;
    --card-shadow: rgba(60, 40, 20, 0.45);
    --foliage-dark: #2f5a1c;
    --foliage-mid: #4f8a2a;
    --blossom: #d8507a;
    --lawn-bright: #6cc234;
    --lawn-deep: #3f9a1e;
    --sky-blue: #4f8fd8;
    --sky-pale: #cfe2f5;
    --stone: #8a7662;
  }
  * { margin: 0; padding: 0; box-sizing: border-box; }
  html, body { width: 1200px; height: 466px; overflow: hidden; }
  body {
    position: relative;
    background: radial-gradient(ellipse at 100% 0%, var(--board-warm) 0%, var(--board-light) 55%, var(--board-light) 100%);
  }
  .concept-card {
    position: absolute;
    width: 468px;
    height: 280px;
    overflow: hidden;
    box-shadow: 4px 5px 9px var(--card-shadow);
  }
  .concept-card--a { left: 82px; top: 90px; }
  .concept-card--b { left: 631px; top: 94px; }

  .scene-zone { position: absolute; left: 0; width: 100%; }

  /* Design A: garden bed over striped lawn */
  .scene-zone--garden-bed {
    top: 0; height: 150px;
    background:
      linear-gradient(180deg, transparent 62%, var(--blossom) 80%, var(--foliage-mid) 100%),
      linear-gradient(90deg, var(--foliage-dark) 0%, var(--foliage-mid) 45%, #6f9a4a 80%, #cfd9c8 100%);
  }
  .scene-zone--lawn-a {
    top: 150px; height: 130px;
    background: linear-gradient(180deg, var(--lawn-bright) 0%, var(--lawn-deep) 100%);
  }

  /* Design B: sky, cottage garden, lawn and path */
  .scene-zone--sky {
    top: 0; height: 120px;
    background: linear-gradient(180deg, var(--sky-blue) 0%, var(--sky-pale) 100%);
  }
  .scene-zone--cottage {
    top: 120px; height: 75px;
    background: linear-gradient(90deg, #2b3a22 0%, var(--foliage-mid) 25%, var(--stone) 60%, var(--foliage-mid) 82%, #4a2f3a 100%);
  }
  .scene-zone--lawn-b {
    top: 195px; height: 85px;
    background: linear-gradient(180deg, var(--lawn-deep) 0%, #5a9a2c 100%);
  }

  .brand-name {
    position: absolute;
    text-align: center;
    color: var(--brand-yellow);
    -webkit-text-stroke: 5px var(--brand-green);
    paint-order: stroke fill;
    white-space: nowrap;
  }
  .brand-name--block {
    font-family: "Archivo Black", "Arial Black", sans-serif;
    font-size: 66px;
    line-height: 56px;
    left: 48px;
    width: 380px;
    top: 18px;
    letter-spacing: -1px;
  }
  .brand-name--wide {
    font-family: "Michroma", sans-serif;
    font-size: 50px;
    line-height: 50px;
    left: 0;
    width: 468px;
    top: 14px;
    letter-spacing: 3px;
    -webkit-text-stroke: 4px var(--brand-green);
  }

  .contact-block {
    position: absolute;
    text-align: center;
    font-family: "PT Sans", "Myriad Pro", sans-serif;
    font-weight: 700;
    color: var(--contact-yellow);
    -webkit-text-stroke: 2.5px var(--brand-green);
    paint-order: stroke fill;
    line-height: 20.5px;
    white-space: nowrap;
  }
  .contact-block--a { left: 34px; width: 400px; top: 190px; }
  .contact-block--b { left: 34px; width: 400px; top: 191px; }
  .contact-offer { font-style: italic; font-size: 16px; }
  .contact-name { font-size: 19px; }
  .contact-phone { font-size: 17px; }
  .contact-email { font-size: 16.5px; }

  .concept-label {
    position: absolute;
    font-family: "Cinzel", serif;
    font-weight: 600;
    font-size: 24px;
    color: var(--label-orange);
    letter-spacing: 1px;
    width: 200px;
    text-align: center;
  }
  .concept-label--a { left: 202px; top: 389px; }
  .concept-label--b { left: 776px; top: 394px; }
</style>
</head>
<body>
  <section class="concept-card concept-card--a">
    <div class="scene-zone scene-zone--garden-bed" role="img" aria-label="Photo of a leafy garden bed with pink and red flowering shrubs"></div>
    <div class="scene-zone scene-zone--lawn-a" role="img" aria-label="Photo of a freshly mown lawn with light and dark stripes"></div>
    <h1 class="brand-name brand-name--block">TIDAL<br>VERGE</h1>
    <div class="contact-block contact-block--a">
      <p class="contact-offer">Call for a free quote</p>
      <p class="contact-name">Darren Quellby</p>
      <p class="contact-phone">0413 562 049</p>
      <p class="contact-email">Email: norma.vance@fernmail.com.au</p>
    </div>
  </section>
  <p class="concept-label concept-label--a">Design A</p>

  <section class="concept-card concept-card--b">
    <div class="scene-zone scene-zone--sky" role="img" aria-label="Photo of a blue sky with white clouds"></div>
    <div class="scene-zone scene-zone--cottage" role="img" aria-label="Photo of a stone cottage framed by trees and a low stone wall"></div>
    <div class="scene-zone scene-zone--lawn-b" role="img" aria-label="Photo of a striped lawn beside a gravel path"></div>
    <h1 class="brand-name brand-name--wide">TIDAL<br>VERGE</h1>
    <div class="contact-block contact-block--b">
      <p class="contact-offer">Call for a free quote</p>
      <p class="contact-name">Darren Quellby</p>
      <p class="contact-phone">0413 562 049</p>
      <p class="contact-email">Email: norma.vance@fernmail.com.au</p>
    </div>
  </section>
  <p class="concept-label concept-label--b">Design B</p>
</body>
</html>
```